Product Sales Brochure Design Project

Tidewell Inks is a line of specialty silk screen inks that use photoluminescent technology to glow in the dark. The inks are primarily used as an accent or decorative feature, and can be used on a variety of garments from T-shirts to pajamas and costumes to couture.
We need a sales brochure, probably tri fold with a finished size of about 8 x 10 or so. We need two versions - one brochure for the bright colors – yellow, green, blue, purple, pink, and one for the neutrals – white that glows blue, royal blue or green, and neutrals (no color) that glow blue, royal blue or green.

Visual Direction:
The brochure needs to visually communicate the wow factor of the inks in a sophisticated and clean manner.

One idea is to use a singular photo or image that sets the stage for what the inks add to a silksccreen project. Perhaps a time elapsed starry sky, or volcano image or fireworks on a city skyline.

The brochure needs to have space inside for color samples to be glued into the center. This will be done by hand at Pellarick. See example below. There will be a little copy on the front and some on the back. This will definitely be light on copy overall. Please use lorem ipsum to hold a place for copy.

The brochures can use the same image/design or can have a design for the colors and one for the neutrals that complement each other.

We will also need a complementary product label that will be about 3” x 8” for the quart containers of ink.
Updates

Project Deadline Extended
Reason: We are still hoping to get some great designs so we've extended the deadline. Very excited to see what you come up with!

Target Market(s)

Tidewell Inks will be sold through distributors to silk screen shops and designers who create printed garments for end users.

Target customer for this brochure is the distributor who will use it as a channel marketing tool to reach silkscreen houses and designers. But the brochure also needs to be usable and inspiring for silkscreeners and designers.

Industry/Entity Type

Royal

Requirements
Must have
• Need to include that Tidewell Inks are made in the USA, patented and eco-friendly. Need a blank space on the back for Distributors to put their own contact sticker or info.

```html
<!DOCTYPE html>
<html lang="en">
<head>
<meta charset="utf-8">
<title>Tidewell Inks – Tri-fold Brochure</title>
<link rel="stylesheet" href="https://fonts.googleapis.com/css2?family=Arimo:wght@400;700&family=Almendra:wght@700&display=swap">
<style>
  :root {
    --sky-top: #0b1038;
    --sky-mid: #1a2b78;
    --city-glow: #1d6f8f;
    --night: #070a22;
    --band: #0c1236;
    --glow-green: #a8cf3a;
    --white: #ffffff;
    --card: rgba(226, 226, 238, 0.9);
    --card-ink: #111633;
    --fold: rgba(200, 210, 255, 0.35);
  }
  * { margin: 0; padding: 0; box-sizing: border-box; }
  html, body { width: 1200px; height: 927px; overflow: hidden; background: #ffffff; }
  body { font-family: "Arimo", Arial, sans-serif; }

  .brochure { position: relative; width: 1200px; height: 927px; overflow: hidden; background: var(--night); }

  .hero-image {
    position: absolute; inset: 0 0 160px 0;
    background:
      radial-gradient(ellipse 220px 140px at 200px 200px, rgba(210, 90, 170, 0.35), transparent 70%),
      radial-gradient(ellipse 200px 130px at 1040px 150px, rgba(220, 90, 80, 0.35), transparent 70%),
      radial-gradient(ellipse 600px 160px at 600px 640px, rgba(40, 150, 190, 0.55), transparent 75%),
      linear-gradient(180deg, var(--sky-top) 0%, #141f5c 30%, var(--sky-mid) 52%, var(--city-glow) 72%, #0d2448 100%);
  }

  .waves { position: absolute; inset: 0; }

  .fold { position: absolute; top: 0; bottom: 0; width: 0; border-left: 1px dashed var(--fold); }
  .fold--left { left: 393px; }
  .fold--right { left: 807px; }

  .feature {
    position: absolute; left: 31px; top: 333px; width: 340px; height: 199px;
    background: var(--night); padding: 16px 18px 0 17px; color: var(--white);
  }
  .feature__title {
    font-family: "Almendra", Georgia, serif; font-weight: 700;
    color: var(--glow-green); font-size: 36px; line-height: 1; margin-bottom: 14px;
  }
  .feature__body { font-size: 18px; line-height: 24px; }

  .distributor {
    position: absolute; left: 415px; top: 31px; width: 370px; height: 501px;
    background: var(--card); color: var(--card-ink); padding: 12px 20px 0 18px;
  }
  .distributor__title { font-size: 26px; font-weight: 700; text-align: center; margin-bottom: 20px; }
  .distributor__field { height: 82px; }
  .distributor__row { display: flex; align-items: flex-end; height: 24px; font-size: 17px; }
  .distributor__row span { white-space: nowrap; margin-right: 4px; }
  .distributor__line { flex: 1; border-bottom: 1px solid var(--card-ink); margin-bottom: 3px; }
  .distributor__extra { height: 32px; border-bottom: 1px solid var(--card-ink); }

  .panel-note {
    position: absolute; top: 842px; width: 393px;
    text-align: center; color: var(--white); font-size: 15px; line-height: 20px;
  }
  .panel-note--left { left: 0; }
  .panel-note--middle { left: 403px; width: 393px; }

  .cover-title {
    position: absolute; left: 807px; width: 393px; top: 750px; text-align: center; color: var(--white);
  }
  .cover-title__brand { font-size: 40px; font-weight: 700; color: var(--glow-green); line-height: 1; margin-bottom: 18px; }
  .cover-title__lead { font-size: 24px; font-weight: 700; line-height: 28px; }
  .cover-title__sub { font-size: 18.5px; line-height: 26px; }
  .cover-title__end { font-size: 24px; font-weight: 700; line-height: 26px; }
</style>
</head>
<body>
<main class="brochure">
  <div class="hero-image" role="img" aria-label="Photo: colourful fireworks bursting over a night-lit city skyline reflected in water"></div>

  <svg class="waves" width="1200" height="927" viewBox="0 0 1200 927" aria-hidden="true">
    <path d="M0 648 C 160 690 320 740 540 748 C 760 755 980 705 1200 668 L1200 690 C 980 728 760 778 540 772 C 320 766 160 716 0 672 Z" fill="var(--band)"/>
    <path d="M0 700 C 180 748 340 792 560 796 C 780 800 990 748 1200 712 L1200 927 L0 927 Z" fill="var(--night)"/>
  </svg>

  <div class="fold fold--left"></div>
  <div class="fold fold--right"></div>

  <section class="feature">
    <h2 class="feature__title">extreme glow</h2>
    <p class="feature__body">Atemolor aut ra velit, omnihicime pria? Tanum sununum tam acredit; et; hoc turnimus, vigitra renate ta, quemediu sente Ici ina menatus eribut Cupiconsus</p>
  </section>

  <section class="distributor">
    <h2 class="distributor__title">Distributor space here</h2>
    <div class="distributor__field">
      <div class="distributor__row"><span>COMPANY NAME</span><i class="distributor__line"></i></div>
      <div class="distributor__extra"></div>
    </div>
    <div class="distributor__field">
      <div class="distributor__row"><span>ADDRESS</span><i class="distributor__line"></i></div>
      <div class="distributor__extra"></div>
    </div>
    <div class="distributor__field">
      <div class="distributor__row"><span>INFO 1</span><i class="distributor__line"></i></div>
      <div class="distributor__extra"></div>
    </div>
    <div class="distributor__field">
      <div class="distributor__row"><span>INFO 2</span><i class="distributor__line"></i></div>
      <div class="distributor__extra"></div>
    </div>
    <div class="distributor__field">
      <div class="distributor__row"><span>INFO 3</span><i class="distributor__line"></i></div>
      <div class="distributor__extra"></div>
      <div class="distributor__extra"></div>
    </div>
  </section>

  <p class="panel-note panel-note--left">Some small text here maybe<br>Atemolor aut ra velit, omnihicime litione res<br>consulii sendam pes condiussis</p>
  <p class="panel-note panel-note--middle">Contact details over here<br>Telephone no. 012 345-6789<br>http://www.website.com</p>

  <section class="cover-title">
    <h1 class="cover-title__brand">Tidewell Inks</h1>
    <p class="cover-title__lead">Specialty silk screen inks</p>
    <p class="cover-title__sub">that use photoluminescent technology</p>
    <p class="cover-title__end">to glow in the dark</p>
  </section>
</main>
</body>
</html>
```